Door Hanger for Bright Harbor Painters

Design a double-sided door hanger that reinforces Bright Harbor Painters’ brand identity while promoting our interior painting services. This piece will be distributed in residential neighborhoods during the winter and should make a strong visual impression at a glance while offering enough detail to motivate follow-up. See attached design brief.

```html
<!DOCTYPE html>
<html lang="en">
<head>
<meta charset="utf-8">
<title>Bright Harbor Painters – Door Hanger</title>
<link href="https://fonts.googleapis.com/css2?family=Montserrat:wght@400;500;600;700&display=swap" rel="stylesheet">
<style>
  :root {
    --bg: #2b2d2b;
    --green: #6f9a55;
    --green-dark: #4f7a3a;
    --ink: #454545;
    --paper: #ffffff;
    --muted: #555555;
  }
  * { box-sizing: border-box; margin: 0; padding: 0; }
  html, body { width: 1200px; height: 2272px; overflow: hidden; background: var(--bg); }
  body { position: relative; font-family: 'Montserrat', sans-serif; }

  .hanger-slot { position: absolute; top: 436px; width: 540px; height: 1399px; filter: drop-shadow(0 6px 10px rgba(0,0,0,.45)); }
  .hanger-slot--front { left: 40px; }
  .hanger-slot--back { left: 620px; }

  .hanger {
    position: absolute; top: 0; left: 0;
    width: 420px; height: 1088px;
    transform: scale(1.2857); transform-origin: 0 0;
    background: var(--paper);
    overflow: hidden;
    clip-path: path(evenodd, "M0 0H420V1088H0Z M-2 95 C50 86 110 90 150 95 A65 65 0 1 1 148 145 C110 160 50 150 -2 145 Z");
  }

  .photo { position: absolute; left: 0; top: 0; width: 420px; height: 720px; }
  .photo--living-room { background: linear-gradient(180deg, #d8d6d1 0%, #c4c2bc 30%, #b9c2c8 50%, #8d8a80 70%, #8a6a48 100%); }
  .photo--great-room { background: linear-gradient(180deg, #cfa877 0%, #e4d9c6 28%, #8fb7d6 42%, #6f6458 65%, #4b4037 100%); }

  .wave { position: absolute; left: 0; top: 0; width: 420px; height: 1088px; }

  .footer-band {
    position: absolute; left: 0; bottom: 0; width: 420px; height: 56px;
    background: var(--green); color: var(--paper);
    display: flex; align-items: center; justify-content: center;
    font-size: 18px; font-weight: 500; letter-spacing: .3px;
  }

  .brand-name {
    position: absolute; left: 0; width: 420px; top: 650px;
    display: flex; align-items: center; justify-content: center; gap: 10px;
    color: var(--green); font-weight: 700; font-size: 24px; line-height: 1.05; text-align: center;
  }
  .brand-name .dot { width: 18px; height: 18px; border-radius: 50%; background: var(--green); flex: none; }

  .headline { position: absolute; left: 0; width: 420px; text-align: center; }
  .headline .line-1 { display: block; font-size: 70px; font-weight: 500; line-height: 66px; letter-spacing: 1px; }
  .headline .line-2 { display: block; font-size: 80px; font-weight: 700; line-height: 70px; }
  .headline--front { top: 770px; }
  .headline--front .line-1 { color: var(--green); }
  .headline--front .line-2 { color: var(--ink); }
  .headline--back { top: 395px; }
  .headline--back .line-1, .headline--back .line-2 { color: var(--paper); text-shadow: 0 2px 6px rgba(0,0,0,.35); }

  .tagline {
    position: absolute; left: 0; width: 420px; top: 925px;
    text-align: center; color: var(--muted); font-size: 29px; line-height: 33px;
  }

  .services-title {
    position: absolute; left: 0; width: 420px; top: 635px;
    text-align: center; color: var(--ink); font-size: 38px; font-weight: 400; letter-spacing: 17px; padding-left: 17px;
  }

  .service-list { position: absolute; top: 712px; left: 36px; width: 370px; display: grid; grid-template-columns: 178px 192px; row-gap: 10px; list-style: none; }
  .service { display: flex; align-items: center; gap: 6px; height: 42px; color: var(--ink); font-size: 15px; font-weight: 600; line-height: 15px; text-transform: uppercase; }
  .service svg { width: 42px; height: 42px; flex: none; }

  .about {
    position: absolute; left: 30px; width: 360px; top: 918px;
    text-align: center; color: var(--muted); font-size: 14px; line-height: 17px; font-weight: 500;
  }
</style>
</head>
<body>

<!-- Front side -->
<div class="hanger-slot hanger-slot--front">
  <section class="hanger hanger--front">
    <div class="photo photo--living-room" role="img" aria-label="Photo of a bright living room with skylights, painted beams and a wall of lake-view windows"></div>
    <svg class="wave" viewBox="0 0 420 1088" aria-hidden="true">
      <path d="M0 690 C20 610 70 560 140 555 C210 550 250 600 300 600 C350 600 390 580 420 550 L420 1088 L0 1088 Z" fill="var(--green)"/>
      <path d="M0 760 C30 660 90 600 170 605 C240 610 270 625 320 618 C370 612 400 590 420 570 L420 1088 L0 1088 Z" fill="var(--paper)"/>
    </svg>
    <div class="brand-name"><span class="dot"></span><span>BRIGHT HARBOR<br>PAINTERS</span></div>
    <h1 class="headline headline--front"><span class="line-1">Interior</span><span class="line-2">Painting</span></h1>
    <p class="tagline">Your trusted choice for<br>interior painting</p>
    <div class="footer-band">www.brightharborpainters.com</div>
  </section>
</div>

<!-- Back side -->
<div class="hanger-slot hanger-slot--back">
  <section class="hanger hanger--back">
    <div class="photo photo--great-room" role="img" aria-label="Photo of a tall great room with timber beams, a ring chandelier and large windows"></div>
    <svg class="wave" viewBox="0 0 420 1088" aria-hidden="true">
      <path d="M0 690 C20 610 70 560 140 555 C210 550 250 600 300 600 C350 600 390 580 420 550 L420 1088 L0 1088 Z" fill="var(--green)"/>
      <path d="M0 760 C30 660 90 600 170 605 C240 610 270 625 320 618 C370 612 400 590 420 570 L420 1088 L0 1088 Z" fill="var(--paper)"/>
    </svg>
    <h2 class="headline headline--back"><span class="line-1">Interior</span><span class="line-2">Painting</span></h2>
    <h3 class="services-title">SERVICES</h3>
    <ul class="service-list">
      <li class="service">
        <svg viewBox="0 0 42 42" aria-hidden="true"><circle cx="21" cy="21" r="19" fill="var(--green)" stroke="var(--green-dark)" stroke-width="3"/><rect x="13" y="12" width="14" height="7" rx="1" fill="#fff"/><path d="M27 15h3v6h-9v3" fill="none" stroke="#fff" stroke-width="2"/><rect x="19" y="24" width="4" height="8" fill="#fff"/></svg>
        <span>Walls</span>
      </li>
      <li class="service">
        <svg viewBox="0 0 42 42" aria-hidden="true"><circle cx="21" cy="21" r="19" fill="var(--green)" stroke="var(--green-dark)" stroke-width="3"/><rect x="12" y="12" width="7" height="5" fill="#fff"/><rect x="22" y="12" width="8" height="5" fill="#fff"/><rect x="12" y="20" width="18" height="10" fill="none" stroke="#fff" stroke-width="2"/><path d="M12 25h18M21 20v10" stroke="#fff" stroke-width="1.5"/></svg>
        <span>Kitchens &amp;<br>Cabinets</span>
      </li>
      <li class="service">
        <svg viewBox="0 0 42 42" aria-hidden="true"><circle cx="21" cy="21" r="19" fill="var(--green)" stroke="var(--green-dark)" stroke-width="3"/><rect x="12" y="12" width="18" height="18" fill="none" stroke="#fff" stroke-width="2"/><path d="M15 16h12M15 20h12M15 24h12" stroke="#fff" stroke-width="1.5"/></svg>
        <span>Ceilings</span>
      </li>
      <li class="service">
        <svg viewBox="0 0 42 42" aria-hidden="true"><circle cx="21" cy="21" r="19" fill="var(--green)" stroke="var(--green-dark)" stroke-width="3"/><path d="M13 28h8v-4h6v-4h4" fill="none" stroke="#fff" stroke-width="3"/><path d="M14 15h14" stroke="#fff" stroke-width="3"/></svg>
        <span>High Access /<br>Stairways</span>
      </li>
      <li class="service">
        <svg viewBox="0 0 42 42" aria-hidden="true"><circle cx="21" cy="21" r="19" fill="var(--green)" stroke="var(--green-dark)" stroke-width="3"/><rect x="15" y="11" width="12" height="20" fill="none" stroke="#fff" stroke-width="2"/><rect x="15" y="11" width="6" height="20" fill="#fff"/><circle cx="24" cy="21" r="1.3" fill="#fff"/></svg>
        <span>Trim &amp; Doors</span>
      </li>
      <li class="service">
        <svg viewBox="0 0 42 42" aria-hidden="true"><circle cx="21" cy="21" r="19" fill="var(--green)" stroke="var(--green-dark)" stroke-width="3"/><rect x="12" y="12" width="18" height="18" fill="#fff"/><path d="M21 12v18M12 21h18" stroke="var(--green)" stroke-width="2"/><path d="M14 28l5-5" stroke="var(--green)" stroke-width="2"/></svg>
        <span>Drywall<br>Repair</span>
      </li>
    </ul>
    <p class="about">Bright Harbor Painters provides a full range of interior painting services for Vermont homes and businesses, taking pride in our clean, communicative workmanship, and friendly, professional tradespeople.</p>
    <div class="footer-band">www.brightharborpainters.com</div>
  </section>
</div>

</body>
</html>
```